Business Card Design Project for Food Export Company

Introduction about my Company Lin Kai Trading Pte. Ltd.
(Lin Kai Food Trading)
A Sole Distributor of various products:
Brand
Soy Powder (Brand: Beanette)
Coffee Powders (Brand: Rovo)
OEM products
- Cocoa Powder
- Green Tea Powder
- Almond Powder
- Almond Flavour Powder
Showing we are professional with decades of experiences in terms of Product Quality and Trust.
NAMECARD - 2 sided namecard
Front:
Informations:
Marcus Tan
Sales Executive
+65 90000000
marcustan@lkfoodtrade.com
Lin Kai Trading Pte. Ltd.
42 Tampines Road, #03-08 Horizon Centre
Singapore 520000
Back:
Sole Distributor:
Beanette and Rovo
OEM Products:
Cocoa Powder / Green Tea Powder / Almond Powder / Almond Flavour Powder / Ice Cream Powder
I have attached Lin Kai Trading's Logos. I've 2 currently, I would like to see some comparison.
Attached 2 Logos for Rovo and Beanette.
Updates
Hi all designers,
I've revised the brief.
Have a look.
Thank you
Marcus

```html
<!DOCTYPE html>
<html lang="en">
<head>
<meta charset="utf-8">
<title>Lin Kai Food Trading – Business Card</title>
<link rel="stylesheet" href="https://fonts.googleapis.com/css2?family=Cinzel:wght@400;600&family=Mulish:ital,wght@0,400;0,700;1,400&display=swap">
<style>
  :root {
    --board: #f4f4f4;
    --board-edge: #e4e4e4;
    --band: #231f20;
    --paper-light: #e9e0c9;
    --paper-mid: #ddd0b0;
    --paper-dark: #cfbf98;
    --ink: #2b2420;
    --ink-soft: #3d332c;
    --accent: #9b1c1f;
    --white: #ffffff;
  }
  * { margin: 0; padding: 0; box-sizing: border-box; }
  html, body { width: 1200px; height: 900px; overflow: hidden; }
  body {
    position: relative;
    background: radial-gradient(ellipse at 50% 30%, #ffffff 0%, var(--board) 55%, var(--board-edge) 100%);
    font-family: "Mulish", sans-serif;
    color: var(--ink);
  }
  .card {
    position: absolute;
    top: 229px;
    width: 419px;
    height: 239px;
    overflow: hidden;
    background:
      radial-gradient(ellipse at 20% 25%, rgba(255,255,255,0.35), transparent 55%),
      radial-gradient(ellipse at 80% 70%, rgba(180,160,115,0.25), transparent 60%),
      linear-gradient(135deg, var(--paper-mid), var(--paper-light) 50%, var(--paper-dark));
    box-shadow: 0 3px 6px rgba(0,0,0,0.22);
  }
  .card--front { left: 150px; }
  .card--back { left: 631px; }

  /* front */
  .brand-mark {
    position: absolute;
    left: 0; right: 0; top: 24px;
    text-align: center;
    z-index: 2;
  }
  .brand-mark__circle {
    display: block;
    margin: 0 auto 5px;
    width: 62px; height: 62px;
    border: 2px solid var(--accent);
    border-radius: 50%;
  }
  .brand-mark__name {
    font-family: "Cinzel", serif;
    font-weight: 400;
    font-size: 14px;
    line-height: 15px;
    color: var(--ink-soft);
  }
  .brand-mark__sub {
    font-family: "Cinzel", serif;
    font-size: 8px;
    line-height: 10px;
    letter-spacing: 1px;
    color: var(--ink-soft);
  }
  .product-list {
    position: absolute;
    left: 0; right: 0; top: 130px;
    z-index: 2;
    text-align: center;
    font-family: "Cinzel", serif;
    font-size: 7.5px;
    line-height: 10.5px;
    color: var(--ink);
  }
  .product-list p + p { margin-top: 1px; }
  .produce-art {
    position: absolute;
    left: 0; bottom: 0;
    z-index: 1;
    width: 419px; height: 95px;
  }

  /* back */
  .holder-name {
    position: absolute;
    left: 50px; top: 36px;
    font-family: "Cinzel", serif;
    font-weight: 400;
    font-size: 21px;
    letter-spacing: 0.5px;
    color: var(--ink);
  }
  .holder-rule {
    position: absolute;
    left: 50px; top: 63px;
    width: 274px; height: 2px;
    background: var(--accent);
  }
  .holder-role {
    position: absolute;
    left: 50px; top: 67px;
    font-weight: 700;
    font-size: 11px;
    letter-spacing: 0.4px;
    color: var(--ink);
  }
  .contact {
    position: absolute;
    left: 50px; top: 89px;
    list-style: none;
    font-size: 13.5px;
    line-height: 17.5px;
    color: var(--ink);
  }
  .company-address {
    position: absolute;
    left: 50px; top: 163px;
    font-style: italic;
    font-size: 10.5px;
    line-height: 13.5px;
    color: var(--ink-soft);
  }
  .faint-mark {
    position: absolute;
    left: 302px; top: 90px;
    width: 118px; height: 118px;
    border: 2px solid rgba(155,130,90,0.25);
    border-radius: 50%;
    display: flex;
    align-items: center;
    justify-content: center;
    font-family: "Cinzel", serif;
    font-weight: 600;
    font-size: 15px;
    color: rgba(155,130,90,0.3);
  }

  /* bottom band */
  .band {
    position: absolute;
    left: 0; top: 695px;
    width: 1200px; height: 205px;
    background: var(--band);
  }
  .band-mark {
    position: absolute;
    left: 852px; top: 58px;
    display: flex;
    align-items: center;
    gap: 10px;
  }
  .band-mark__circle {
    width: 88px; height: 88px;
    border: 3px solid var(--accent);
    border-radius: 50%;
  }
  .band-mark__name {
    font-family: "Cinzel", serif;
    font-weight: 400;
    font-size: 30px;
    line-height: 30px;
    color: var(--white);
  }
  .band-mark__sub {
    margin-top: 3px;
    font-family: "Cinzel", serif;
    font-size: 11px;
    line-height: 12px;
    letter-spacing: 1px;
    color: var(--white);
  }
</style>
</head>
<body>

<section class="card card--front">
  <div class="brand-mark">
    <span class="brand-mark__circle"></span>
    <p class="brand-mark__name">LIN KAI</p>
    <p class="brand-mark__sub">FOOD TRADING</p>
  </div>
  <div class="product-list">
    <p>SOLE DISTRIBUTOR: BEANETTE AND ROVO</p>
    <p>OEM PRODUCTS: COCOA POWDER · GREEN TEA POWDER<br>
       ALMOND POWDER · ALMOND FLAVOUR POWDER<br>
       ICE CREAM POWDER</p>
  </div>
  <svg class="produce-art" viewBox="0 0 419 95" role="img" aria-label="Illustration of a pile of soybeans on the left and a heap of cocoa powder with coffee beans on the right">
    <defs>
      <linearGradient id="produce-fill" x1="0" x2="1" y1="0" y2="0">
        <stop offset="0" stop-color="#d4b688"/>
        <stop offset="0.5" stop-color="#bf9a66"/>
        <stop offset="0.6" stop-color="#6e4330"/>
        <stop offset="1" stop-color="#4e2d20"/>
      </linearGradient>
    </defs>
    <path d="M0 44 C60 34 150 36 215 48 C250 40 290 33 330 34 C370 35 400 38 419 40 L419 95 L0 95 Z" fill="url(#produce-fill)"/>
  </svg>
</section>

<section class="card card--back">
  <h1 class="holder-name">MARCUS TAN</h1>
  <div class="holder-rule"></div>
  <p class="holder-role">SALES EXECUTIVE</p>
  <ul class="contact">
    <li>(+65) 90000000</li>
    <li>marcustan@lkfoodtrade.com</li>
    <li>www.linkaiwebsitehere.com</li>
  </ul>
  <p class="company-address">
    Lin Kai Trading Pte. Ltd.<br>
    Address: 42 Tampines Road,<br>
    #03-08 Horizon Centre<br>
    Singapore 520000
  </p>
  <div class="faint-mark">LIN KAI</div>
</section>

<footer class="band">
  <div class="band-mark">
    <span class="band-mark__circle"></span>
    <div>
      <p class="band-mark__name">LIN<br>KAI</p>
      <p class="band-mark__sub">FOOD TRADING</p>
    </div>
  </div>
</footer>

</body>
</html>
```